Business Card Design Project

- makeup artist business card

- original and creative

- Elegant design

- Feel free to come out with cool designs but stick to being elegant and attractive

- Design relates to makeup

- includes name, occupation, contact numbers, email, website

- regular size business card

- round corner card

- double sided

- on 1 side it should just have the website name in the center " velvetbrushhue.com "

Industry/Entity Type

Business

Requirements
Must have
• Marla Tobin
Makeup Artist
USA: +1 (213)555-0147
Singapore: +65 90007312
marlatobin@velvetbrushhue.com
www.velvetbrushhue.com
Should not have
• nothing cartoon looking.
Pictures of makeup being grab from the internet.. Examples: eyes or lips.

```html
<!DOCTYPE html>
<html lang="en">
<head>
<meta charset="utf-8">
<title>Marla Tobin – Makeup Artist Business Card</title>
<link rel="stylesheet" href="https://fonts.googleapis.com/css2?family=Questrial&display=swap">
<style>
  :root {
    --backdrop: #ece8e4;
    --card: #ffffff;
    --ink-grey: #6e6e6e;
    --ink-soft: #8a8a8a;
    --rose-name: #e0638e;
    --tone-blush: #eeaab8;
    --tone-berry: #e8799d;
    --tone-peach: #e4a88a;
    --tone-nude: #edbfb3;
    --card-shadow: 0 10px 28px rgba(0, 0, 0, 0.18);
  }
  * { margin: 0; padding: 0; box-sizing: border-box; }
  html, body {
    width: 1200px;
    height: 900px;
    overflow: hidden;
    background: var(--backdrop);
    font-family: "Questrial", "Century Gothic", sans-serif;
  }
  .stage {
    position: relative;
    width: 1200px;
    height: 900px;
  }
  .card {
    position: absolute;
    top: 295px;
    width: 540px;
    height: 310px;
    background: var(--card);
    border-radius: 22px;
    box-shadow: var(--card-shadow);
  }
  .card--front { left: 40px; }
  .card--back { left: 620px; }

  /* Front side */
  .identity {
    position: absolute;
    top: 62px;
    left: 150px;
    width: 300px;
    text-align: center;
  }
  .identity__name {
    font-size: 31px;
    font-variant: small-caps;
    letter-spacing: 1px;
    color: var(--rose-name);
    font-weight: 400;
    line-height: 1;
  }
  .identity__role {
    margin-top: 4px;
    padding-left: 70px;
    font-size: 16px;
    color: var(--ink-grey);
    letter-spacing: 0.5px;
  }
  .contacts {
    position: absolute;
    left: 30px;
    bottom: 20px;
    list-style: none;
    font-size: 13px;
    color: var(--ink-soft);
    line-height: 30px;
    letter-spacing: 0.3px;
  }
  .shade-field {
    position: absolute;
    left: 290px;
    top: 176px;
    width: 236px;
    height: 120px;
    border-radius: 10px;
    background: linear-gradient(90deg, var(--tone-blush), var(--tone-berry) 45%, var(--tone-peach) 75%, var(--tone-nude));
  }

  /* Back side */
  .back-name {
    position: absolute;
    top: 34px;
    left: 0;
    width: 100%;
    text-align: center;
    font-size: 17px;
    font-variant: small-caps;
    letter-spacing: 1px;
    color: var(--rose-name);
  }
  .website {
    position: absolute;
    top: 120px;
    left: 0;
    width: 100%;
    text-align: center;
    font-size: 24px;
    color: var(--ink-grey);
    letter-spacing: 0.5px;
  }
  .shade-band {
    position: absolute;
    top: 215px;
    left: 156px;
    width: 228px;
    height: 36px;
    border-radius: 18px;
    background: linear-gradient(90deg, var(--tone-peach), var(--tone-nude) 30%, var(--tone-berry) 55%, var(--tone-blush));
  }
</style>
</head>
<body>
  <main class="stage">
    <section class="card card--front" aria-label="Business card front">
      <div class="identity">
        <h1 class="identity__name">Marla Tobin</h1>
        <p class="identity__role">makeup artist</p>
      </div>
      <ul class="contacts">
        <li>USA: +1 (213)555-0147</li>
        <li>Singapore: +65 90007312</li>
        <li>marlatobin@velvetbrushhue.com</li>
      </ul>
      <div class="shade-field" role="img" aria-label="Decorative area of blush, berry, peach and nude makeup shades"></div>
    </section>

    <section class="card card--back" aria-label="Business card back">
      <p class="back-name">Marla Tobin</p>
      <p class="website">www.velvetbrushhue.com</p>
      <div class="shade-band" role="img" aria-label="Decorative band of peach, nude, berry and blush makeup shades"></div>
    </section>
  </main>
</body>
</html>
```